依頼詳細
以前こちらで作成して頂いた雰囲気の内容でお願いします。
※添付チラシ

記載項目
・もえぎうたのロゴマークを入れてください。
https://moegiuta.or.jp/event-t/2020-03-14-2 このアドレス用のQRコードを記載してください。
・添付しました画像を使用してください。
サイズ
A4
ページ数
片面
希望イメージ
シンプル 複雑
単色 カラフル
暗い 明るい
日常 高級
遊び心 厳粛
未来的 伝統的
女性的 男性的
希望する色
納品ファイル
補足説明
■ 選んだ理由

ご提案いただきありがとうございました。
どれも良いご提案で悩みましたが、色合いや、雰囲気、読みやすさ、
これから家づくりを考える対象年齢層などを考慮して
選択させて頂きました。

■ 提案者全員のお礼・コメント

多くのご提案を頂きありがとうございました。<m(__)m>

```html
<!DOCTYPE html>
<html lang="ja">
<head>
<meta charset="utf-8">
<title>家づくりはじめの一歩 セミナー</title>
<link href="https://fonts.googleapis.com/css2?family=M+PLUS+Rounded+1c:wght@500;800&family=Noto+Sans+JP:wght@400;500;700;900&display=swap" rel="stylesheet">
<style>
:root{
  --orange:#ee7b1b;
  --orange-deep:#e0600f;
  --cream:#fff6e8;
  --pale:#fdeccf;
  --ink:#3a3330;
  --grey:#6d6460;
  --white:#ffffff;
}
*{box-sizing:border-box;margin:0;padding:0}
html,body{width:848px;height:1200px;overflow:hidden;background:var(--white)}
body{font-family:"Noto Sans JP",sans-serif;color:var(--ink);position:relative}
.hero{position:absolute;left:0;top:0;width:848px;height:360px;
  background:linear-gradient(160deg,#fbf3e6 0%,#f2dcc0 45%,#e9c9a4 75%,#f6e6d0 100%)}
.tag{position:absolute;left:26px;top:0;width:40px;height:220px;background:var(--orange);
  color:var(--white);writing-mode:vertical-rl;font-size:14px;font-weight:700;
  display:flex;align-items:center;justify-content:center;letter-spacing:1px;white-space:nowrap}
.title-block{position:absolute;left:90px;top:18px;width:740px;text-align:center}
.title{font-family:"M PLUS Rounded 1c",sans-serif;font-weight:800;font-size:60px;color:var(--orange);letter-spacing:2px}
.title .bracket{color:var(--orange-deep)}
.subtitle{margin-top:4px;font-size:25px;font-weight:700;color:var(--grey);letter-spacing:2px}
.mascot{position:absolute;left:556px;top:170px;width:104px;height:104px;border-radius:50%;
  background:var(--white);border:3px solid var(--orange);display:flex;align-items:center;justify-content:center;
  font-size:15px;font-weight:700;color:var(--orange)}
.bubble{position:absolute;left:672px;top:156px;width:160px;height:140px;background:var(--white);
  border:2px solid var(--orange);border-radius:8px;padding:8px 10px;font-size:9.5px;line-height:1.55;color:var(--grey)}
.bubble b{display:block;font-size:13px;color:var(--orange);margin-bottom:3px}
.points{position:absolute;left:28px;top:380px;width:792px;display:flex;gap:22px}
.point{flex:1;font-size:12.5px;line-height:1.8;color:var(--ink)}
.point .initial{float:left;width:38px;height:38px;margin:2px 8px 2px 0;background:var(--orange);color:var(--white);
  font-size:25px;font-weight:900;display:flex;align-items:center;justify-content:center}
.point em{font-style:normal;color:var(--orange-deep);font-weight:700}
.reason{position:absolute;left:28px;top:540px;width:792px;height:250px;display:flex;gap:18px}
.reason-text{width:340px;font-size:15px;font-weight:700;line-height:1.7;padding-top:10px}
.reason-text .lead{color:var(--orange);font-size:14px}
.reason-text h2{font-size:19px;border-bottom:2px dashed var(--orange);padding-bottom:4px;margin-bottom:8px}
.reason-text mark{background:var(--pale);color:var(--orange-deep)}
.lecture{flex:1;border:3px solid var(--orange);border-radius:10px;padding:12px 18px;background:var(--cream)}
.lecture h3{color:var(--orange-deep);font-size:20px;font-weight:900;text-align:center;margin-bottom:8px}
.lecture h3 span{background:linear-gradient(transparent 60%,#ffe08a 60%)}
.lecture li{list-style:none;font-size:14.5px;font-weight:700;line-height:1.62}
.lecture li::before{content:"■";color:var(--orange);margin-right:6px}
.date-band{position:absolute;left:0;top:810px;width:848px;height:96px;background:var(--cream);
  border-top:3px solid var(--orange);border-bottom:3px solid var(--orange);display:flex;align-items:center;padding-left:28px}
.date-label{background:var(--orange);color:var(--white);font-size:13px;font-weight:700;padding:6px 8px;border-radius:4px;line-height:1.2;text-align:center}
.date-label small{display:block;font-size:11px}
.date-main{margin-left:14px;color:var(--orange-deep);font-weight:900;font-size:54px;letter-spacing:-1px}
.date-main .dow{display:inline-block;width:34px;height:34px;border-radius:50%;background:var(--orange);color:var(--white);
  font-size:20px;text-align:center;line-height:34px;vertical-align:middle;margin-left:4px}
.time{margin-left:20px;color:var(--orange-deep);font-weight:900;font-size:38px;line-height:1}
.time small{display:block;font-size:13px;color:var(--grey);font-weight:700;text-align:center;margin-top:4px}
.badge{position:absolute;top:7px;width:76px;height:76px;border-radius:50%;background:var(--orange);color:var(--white);
  font-size:14px;font-weight:900;display:flex;align-items:center;justify-content:center;text-align:center;line-height:1.2}
.badge.free{left:664px}
.badge.kids{left:752px;background:var(--white);color:var(--orange);border:3px solid var(--orange)}
.info{position:absolute;left:28px;top:935px;width:380px;font-size:14px}
.info dl{display:grid;grid-template-columns:76px 1fr;row-gap:16px}
.info dt{background:var(--orange);color:var(--white);font-weight:700;text-align:center;border-radius:3px;padding:2px 0;align-self:start}
.info dd{padding-left:12px;line-height:1.5}
.info dd strong{font-size:17px}
.contact{position:absolute;left:430px;top:935px;width:390px;font-size:13px}
.contact .note{font-size:12px;color:var(--grey);margin-bottom:8px}
.contact .row{display:flex;align-items:center;gap:8px;margin-bottom:6px}
.contact .phone{font-size:28px;font-weight:900;color:var(--orange-deep)}
.contact .fax{font-size:22px;font-weight:900;color:var(--ink)}
.contact .lbl{background:var(--ink);color:var(--white);font-size:11px;font-weight:700;padding:2px 5px;border-radius:3px}
.qr{position:absolute;right:0;top:26px;width:92px;text-align:center;font-size:11px;font-weight:700;color:var(--grey)}
.qr .code{width:92px;height:92px;margin-top:4px;background:var(--white);border:2px solid var(--ink)}
.org{margin-top:22px;border-top:1px solid var(--orange);padding-top:12px;display:flex;align-items:center;gap:10px}
.org .sq{width:28px;height:28px;border-radius:50%;background:var(--orange)}
.org p{font-size:12px;color:var(--grey);line-height:1.3}
.org p b{display:block;font-size:18px;color:var(--ink)}
</style>
</head>
<body>
<section class="hero" role="img" aria-label="家の模型を手に笑顔で並ぶ家族の写真"></section>
<div class="tag">暮らしの「学び場」セミナー</div>
<header class="title-block">
  <h1 class="title"><span class="bracket">[</span>家づくり<span class="bracket">]</span>はじめの一歩</h1>
  <p class="subtitle">後悔しないために学ぶ2つの準備</p>
</header>
<div class="mascot">もえぎうた</div>
<div class="bubble"><b>もえぎうたくん</b>家づくりの不安や疑問に寄り添う、もえぎうたのナビゲーターです。はじめての方も気軽に参加してね。</div>

<section class="points">
  <div class="point"><span class="initial">家</span>を建てることは人生の大きな目標。しかし<em>ゴールではなくスタート</em>です。建てた後の暮らしを見据え、後悔のない住まいづくりの準備をしましょう。</div>
  <div class="point"><span class="initial">ま</span>ずは自分たちの理想の暮らしを考え、家族の想いを整理することが大切です。<em>「どうやって始めればいいの？」</em>という疑問にお答えします。</div>
  <div class="point"><span class="initial">そ</span>して資金計画や土地選びなど、知っておくべきポイントを専門家が解説。<em>当会認定講師</em>が中立の立場でわかりやすくお伝えします。</div>
</section>

<section class="reason">
  <div class="reason-text">
    <p class="lead">だから</p>
    <h2>家づくりを始める前に<br>知っておくべきこと</h2>
    <p>知ってみると簡単なことだけど、なかなか見えないものの<mark>「家づくりはじめの一歩」</mark>にすべきことを盛り沢山でお届けする<mark>90分</mark></p>
  </div>
  <div class="lecture">
    <h3><span>当会認定講師がわかりやすく説明します。</span></h3>
    <ul>
      <li>暮らすベースはたった3種類</li>
      <li>住宅購入を検討する5つの質問</li>
      <li>土地を買う前に必要なこと</li>
      <li>価格を書く前に必要なこと</li>
      <li>見積りをする前に必要なこと</li>
      <li>住宅会社の探し方と選択基準</li>
      <li>自分の住宅予算は自分がもてる価格</li>
    </ul>
  </div>
</section>

<section class="date-band">
  <div class="date-label">開催日<small>2020年</small></div>
  <div class="date-main">3/14<span class="dow">土</span></div>
  <div class="time">13:30 ▶ 15:00<small>（受付 13:00〜）</small></div>
  <div class="badge free">参加費<br>無料</div>
  <div class="badge kids">お子様<br>連れ<br>参加OK</div>
</section>

<section class="info">
  <dl>
    <dt>参加費</dt><dd><strong>無 料</strong></dd>
    <dt>会 場</dt><dd><strong>木漏れ日の家</strong><br>金沢市緑ヶ丘2丁目5番地</dd>
    <dt>講 師</dt><dd>もえぎうた認定講師</dd>
    <dt>定 員</dt><dd>先着10名</dd>
  </dl>
</section>

<section class="contact">
  <p class="note">電話、ホームページにてお申し込みください。</p>
  <div class="row">
    <svg width="28" height="28" viewBox="0 0 24 24" aria-hidden="true"><path fill="#e0600f" d="M6.6 10.8a15 15 0 0 0 6.6 6.6l2.2-2.2a1 1 0 0 1 1-.25 11.4 11.4 0 0 0 3.6.57 1 1 0 0 1 1 1V20a1 1 0 0 1-1 1A17 17 0 0 1 3 4a1 1 0 0 1 1-1h3.5a1 1 0 0 1 1 1c0 1.25.2 2.45.57 3.57a1 1 0 0 1-.25 1z"/></svg>
    <span class="phone">0120-555-018</span>
  </div>
  <div class="row"><span class="lbl">FAX</span><span class="fax">06-0000-4417</span></div>
  <div class="qr">WEB予約<div class="code" role="img" aria-label="予約ページ https://moegiuta.or.jp/event-t/2020-03-14-2 へのQRコード"></div></div>
  <div class="org">
    <span class="sq"></span>
    <p>主催 一般社団法人<b>暮らし設計支援機構 もえぎうた</b></p>
  </div>
</section>
</body>
</html>
```